Tirovel

We need a business card for our company is a holding for different business all are different we try to have some air of relax and fun in our projects we add pictures of the office to give you an idea od the mood of the business

Business

```html
<!DOCTYPE html>
<html lang="en">
<head>
<meta charset="utf-8">
<title>Tirovel business card</title>
<link rel="stylesheet" href="https://fonts.googleapis.com/css2?family=Open+Sans:wght@600;700;800&display=swap">
<style>
  :root {
    --backdrop: #d8c436;
    --wood-dark: #341a0a;
    --wood-mid: #4a2712;
    --wood-light: #573018;
    --banana-light: #f3d25a;
    --banana-deep: #dca42a;
    --leaf-light: #48a046;
    --leaf-deep: #246f2a;
    --brand-yellow: #f2e42a;
    --ink-white: #ffffff;
  }
  html, body {
    margin: 0;
    width: 1200px;
    height: 898px;
    overflow: hidden;
    background: var(--backdrop);
    font-family: "Open Sans", Arial, sans-serif;
  }
  .card {
    position: absolute;
    left: 350px;
    top: 39px;
    width: 500px;
    height: 820px;
    overflow: hidden;
    background: linear-gradient(160deg, var(--wood-light) 0%, var(--wood-mid) 45%, var(--wood-dark) 100%);
    box-shadow: 0 18px 40px rgba(60, 45, 0, 0.35);
  }
  .photo-banana {
    position: absolute;
    left: 0;
    top: 0;
    width: 190px;
    height: 330px;
    background: linear-gradient(150deg, var(--banana-light), var(--banana-deep));
  }
  .photo-leaves {
    position: absolute;
    left: 160px;
    top: 350px;
    width: 340px;
    height: 470px;
    background: linear-gradient(150deg, var(--leaf-light), var(--leaf-deep));
  }
  .brand {
    position: absolute;
    left: 468px;
    top: 60px;
    transform-origin: 0 0;
    transform: rotate(90deg);
    display: flex;
    align-items: center;
    gap: 14px;
    white-space: nowrap;
  }
  .brand-square {
    width: 30px;
    height: 30px;
    background: var(--brand-yellow);
  }
  .brand-name {
    color: var(--brand-yellow);
    font-size: 44px;
    font-weight: 800;
    line-height: 1;
  }
  .holder-name {
    position: absolute;
    left: 448px;
    top: 470px;
    transform-origin: 0 0;
    transform: rotate(90deg);
    color: var(--ink-white);
    font-size: 32px;
    font-weight: 700;
    white-space: nowrap;
    line-height: 1;
  }
  .contact {
    position: absolute;
    left: 122px;
    top: 560px;
    transform-origin: 0 0;
    transform: rotate(90deg);
    color: var(--ink-white);
    font-size: 22px;
    font-weight: 600;
    line-height: 32px;
    white-space: nowrap;
  }
  .contact-row {
    display: flex;
    align-items: center;
    gap: 10px;
  }
  .contact-icon {
    width: 18px;
    height: 18px;
    flex: none;
  }
</style>
</head>
<body>
  <main class="card">
    <div class="photo-banana" role="img" aria-label="Photograph of a ripe yellow banana"></div>
    <div class="photo-leaves" role="img" aria-label="Photograph of green banana leaves"></div>

    <div class="brand">
      <span class="brand-square"></span>
      <span class="brand-name">Tirovel</span>
    </div>

    <div class="holder-name">Mara Quell</div>

    <div class="contact">
      <div class="contact-row">
        <span>[000] 4821 3096</span>
        <svg class="contact-icon" viewBox="0 0 20 20" aria-label="Phone">
          <path d="M5 2 L8 2 L9 6 L7 8 C8 11 9 12 12 13 L14 11 L18 12 L18 15 C18 17 16 18 14 18 C8 17 3 12 2 6 C2 4 3 2 5 2 Z" fill="none" stroke="currentColor" stroke-width="1.6"/>
        </svg>
      </div>
      <div class="contact-row">
        <span>mara@tirovel.com</span>
        <svg class="contact-icon" viewBox="0 0 20 20" aria-label="Email">
          <rect x="2" y="4" width="16" height="12" fill="none" stroke="currentColor" stroke-width="1.6"/>
          <path d="M2 4 L10 11 L18 4" fill="none" stroke="currentColor" stroke-width="1.6"/>
        </svg>
      </div>
    </div>
  </main>
</body>
</html>
```